Mr Tovel Car Wash Menu Brochure

Front/Back brochure with Car Wash Menu Options & pricing
(size : 8.5" x 3.66" - front/back)

Side 1:
Logo on top
"Wash Menu"
- Grand Tovel - $19
- includes Orla & Finch
- Super Shine Hot Wax
- Kestrel Coat - total surface sealant
- Wheel Bright
- Orla & Finch - $15
- Includes Prime Tovel
- Clear Coat Protectant
- Tire Gloss
- Prime Tovel - $11
- Includes Express Wash
- Triple Foam
- Wheel Cleaner
- Express Wash - $4

*Add-Ons
- Dravenol Ceramic - $5
- Kestrel Coat - $3
- Tire Gloss - $3

*FREE Vacuums with every purchase
* We care about the earth! We recycle our water

SIDE 2:
Mr Tovel Logo on Top
Unlimited Monthly VIP Club
- Grand Tovel - $55
- includes 10% off detail packages
- Orla & Finch - $45
-Prime Tovel - $30
-Express Wash - $20

* one wash tag per vehicle

Target Market(s)

sophisticated customers

Industry/Entity Type

car wash

Colors
0054AA
0677BA
7BADD7
CADEEF
E8F1F8
EE7325
F08F49
F5BC92
FAE3D3
FDF4ED

Requirements
Must have
• pictures/icons to relay what each package entails

```html
<!DOCTYPE html>
<html lang="en">
<head>
<meta charset="utf-8">
<title>Mr Tovel – Wash Menu Rack Cards</title>
<link rel="stylesheet" href="https://fonts.googleapis.com/css2?family=Barlow+Condensed:ital,wght@1,800&family=Exo+2:ital,wght@0,400;0,900;1,400;1,800;1,900&display=swap">
<style>
  :root {
    --red: #d8261a;
    --red-dark: #9e170e;
    --blue: #17408f;
    --blue-bright: #0054aa;
    --cyan: #2aa6df;
    --ink: #0d0d0f;
    --paper: #ffffff;
    --paper-shade: #e4e6ea;
    --stage: #e9e9ea;
  }
  * { box-sizing: border-box; margin: 0; padding: 0; }
  html, body { width: 1200px; height: 1200px; overflow: hidden; }
  body { background: var(--stage); position: relative; font-family: "Exo 2", sans-serif; }

  .card {
    position: absolute; top: 112px;
    width: 677px; height: 1571px;
    transform: scale(0.62); transform-origin: 0 0;
    overflow: hidden; color: var(--paper);
    box-shadow: 0 12px 40px rgba(0,0,0,.35);
  }
  .card--menu { left: 125px; }
  .card--club { left: 655px; }
  .card__bg { position: absolute; inset: 0; width: 100%; height: 100%; }
  .abs { position: absolute; line-height: 1; white-space: nowrap; }

  /* brand */
  .brand { position: absolute; left: 0; right: 0; top: 120px; display: flex; justify-content: center; align-items: center; gap: 18px; }
  .brand__dot { width: 30px; height: 30px; border-radius: 50%; background: var(--red); }
  .brand__name { font-weight: 900; font-size: 92px; color: var(--blue-bright); letter-spacing: 1px; line-height: 1; }
  .brand__tag { position: absolute; left: 0; right: 0; top: 232px; text-align: center; font-size: 24px; letter-spacing: 8px; color: var(--red); }

  /* headings */
  .banner-title { font-family: "Barlow Condensed", sans-serif; font-style: italic; font-weight: 800; }
  .menu-title { left: 105px; width: 470px; top: 298px; text-align: center; font-size: 74px; }

  /* packages */
  .pkg-name { font-style: italic; font-weight: 900; font-size: 37px; }
  .pkg-line { position: absolute; height: 0; border-top: 2px solid var(--cyan); }
  .price {
    position: absolute; width: 125px; height: 48px;
    clip-path: polygon(16% 0, 100% 0, 84% 100%, 0 100%);
    display: flex; align-items: center; justify-content: center;
    font-style: italic; font-weight: 900; font-size: 37px;
  }
  .price--red { background: linear-gradient(90deg, var(--red-dark), var(--red)); }
  .price--blue { background: linear-gradient(90deg, var(--blue), var(--blue-bright)); }
  .feature { font-style: italic; font-weight: 800; font-size: 24px; }
  .feature::before { content: "»"; color: var(--cyan); font-weight: 900; margin-right: 12px; font-size: 30px; }
  .addon { font-style: italic; font-weight: 800; font-size: 29px; }
  .addon::before { content: "»"; color: #d9d9d9; margin-right: 12px; font-size: 34px; }
  .addons-title { left: 68px; top: 1070px; font-style: italic; font-weight: 900; font-size: 54px; }

  /* contact */
  .cta { font-style: italic; font-weight: 900; font-size: 60px; text-align: center; }
  .phone { display: flex; align-items: center; gap: 16px; font-style: italic; font-weight: 900; font-size: 64px; }
  .phone__icon { width: 46px; height: 46px; }
  .footnote { left: 0; right: 0; text-align: center; font-style: italic; font-weight: 800; font-size: 24px; }
  .tag-note { font-size: 22px; font-weight: 400; }

  .photo-slot {
    position: absolute; left: 0; top: 300px; width: 677px; height: 500px;
    background: linear-gradient(120deg, #3a3d42 0%, #6d7075 40%, #c9cdd2 75%, #e6e8ea 100%);
    clip-path: polygon(37% 0, 100% 0, 100% 100%, 0 100%, 0 6%);
  }
</style>
</head>
<body>

<!-- Side 1: wash menu -->
<section class="card card--menu">
  <svg class="card__bg" viewBox="0 0 677 1571" preserveAspectRatio="none" aria-hidden="true">
    <defs>
      <linearGradient id="sheenA" x1="0" y1="0" x2="0" y2="1">
        <stop offset="0" stop-color="#ffffff"/><stop offset=".35" stop-color="#eef0f3"/>
        <stop offset=".8" stop-color="#c9ccd2"/><stop offset="1" stop-color="#5c5e66"/>
      </linearGradient>
      <linearGradient id="redA" x1="0" y1="0" x2="1" y2="0">
        <stop offset="0" stop-color="#a8180e"/><stop offset="1" stop-color="#e1281a"/>
      </linearGradient>
    </defs>
    <rect width="677" height="1571" fill="url(#sheenA)"/>
    <polygon points="0,290 90,270 0,470" fill="var(--blue)"/>
    <polygon points="150,300 585,300 550,383 115,383" fill="#8a8d94"/>
    <polygon points="140,292 575,292 540,375 105,375" fill="url(#redA)"/>
    <polygon points="75,359 677,359 677,710 520,1044 0,1044 0,500" fill="var(--ink)"/>
    <polygon points="677,742 677,1270 446,1270" fill="var(--blue)"/>
    <polygon points="0,1044 540,1044 440,1270 677,1270 677,1290 90,1290 0,1140" fill="url(#redA)"/>
    <polygon points="0,1410 60,1410 95,1455 520,1455 475,1571 0,1571" fill="var(--blue)"/>
    <polygon points="40,1290 605,1290 575,1372 75,1372" fill="var(--blue)"/>
    <polygon points="95,1372 615,1372 650,1455 130,1455" fill="url(#redA)"/>
    <polygon points="0,1550 245,1550 240,1571 0,1571" fill="var(--red)"/>
  </svg>

  <div class="brand"><span class="brand__dot"></span><span class="brand__name">MR TOVEL</span></div>
  <p class="brand__tag">EXPRESS WASH &amp; DETAIL</p>

  <h1 class="abs banner-title menu-title">WASH MENU</h1>

  <!-- Grand Tovel -->
  <h2 class="abs pkg-name" style="left:100px;top:412px">GRAND TOVEL</h2>
  <span class="pkg-line" style="left:75px;top:455px;width:360px"></span>
  <span class="pkg-line" style="left:455px;top:406px;width:155px"></span>
  <span class="price price--red" style="left:440px;top:412px">$19</span>
  <p class="abs feature" style="left:75px;top:473px">includes Orla &amp; Finch</p>
  <p class="abs feature" style="left:75px;top:507px">Super Shine Hot Wax</p>
  <p class="abs feature" style="left:75px;top:546px">Kestrel Coat - total surface sealant</p>
  <p class="abs feature" style="left:75px;top:580px">Wheel Bright</p>

  <!-- Orla & Finch -->
  <h2 class="abs pkg-name" style="left:100px;top:630px">ORLA &amp; FINCH</h2>
  <span class="pkg-line" style="left:75px;top:673px;width:360px"></span>
  <span class="pkg-line" style="left:455px;top:623px;width:155px"></span>
  <span class="price price--red" style="left:440px;top:629px">$15</span>
  <p class="abs feature" style="left:75px;top:689px">Includes Prime Tovel</p>
  <p class="abs feature" style="left:75px;top:724px">Clear Coat Protectant</p>
  <p class="abs feature" style="left:75px;top:758px">Tire Gloss</p>

  <!-- Prime Tovel -->
  <h2 class="abs pkg-name" style="left:100px;top:802px">PRIME TOVEL</h2>
  <span class="pkg-line" style="left:75px;top:845px;width:360px"></span>
  <span class="pkg-line" style="left:455px;top:792px;width:155px"></span>
  <span class="price price--red" style="left:440px;top:798px">$11</span>
  <p class="abs feature" style="left:75px;top:859px">Includes Express Wash</p>
  <p class="abs feature" style="left:75px;top:892px">Triple Foam</p>
  <p class="abs feature" style="left:75px;top:926px">Wheel Cleaner</p>

  <!-- Express Wash -->
  <h2 class="abs pkg-name" style="left:100px;top:972px">EXPRESS WASH</h2>
  <span class="pkg-line" style="left:75px;top:1015px;width:360px"></span>
  <span class="pkg-line" style="left:455px;top:965px;width:155px"></span>
  <span class="price price--red" style="left:440px;top:971px">$4</span>

  <!-- Add-ons -->
  <h2 class="abs addons-title">*ADD-ONS</h2>
  <span class="pkg-line" style="left:60px;top:1128px;width:262px;border-color:#fff"></span>
  <span class="pkg-line" style="left:340px;top:1090px;width:150px;border-color:#fff"></span>
  <p class="abs addon" style="left:80px;top:1145px">Dravenol Ceramic - $5</p>
  <p class="abs addon" style="left:80px;top:1187px">Kestrel Coat - $3</p>
  <p class="abs addon" style="left:80px;top:1229px">Tire Gloss - $3</p>

  <p class="abs cta" style="left:40px;width:590px;top:1303px">CALL US NOW</p>
  <p class="abs phone" style="left:150px;top:1380px">
    <svg class="phone__icon" viewBox="0 0 48 48" aria-hidden="true"><circle cx="24" cy="24" r="21" fill="none" stroke="#fff" stroke-width="3"/><path d="M17 13c2-1 3 0 4 3s0 3-1 4c1 3 4 6 7 7 1-1 2-2 4-1s4 2 3 4c-1 3-4 4-7 3-6-2-11-7-13-13-1-3 1-6 3-7z" fill="#fff"/></svg>
    0456 812 307
  </p>
  <p class="abs footnote" style="top:1470px">*FREE Vacuums with every purchase</p>
  <p class="abs footnote" style="top:1504px">* We care about the earth! We recycle our water</p>
</section>

<!-- Side 2: VIP club -->
<section class="card card--club">
  <svg class="card__bg" viewBox="0 0 677 1571" preserveAspectRatio="none" aria-hidden="true">
    <defs>
      <linearGradient id="sheenB" x1="0" y1="0" x2="0" y2="1">
        <stop offset="0" stop-color="#ffffff"/><stop offset=".35" stop-color="#eef0f3"/>
        <stop offset=".8" stop-color="#c9ccd2"/><stop offset="1" stop-color="#5c5e66"/>
      </linearGradient>
      <linearGradient id="redB" x1="0" y1="0" x2="1" y2="1">
        <stop offset="0" stop-color="#e1281a"/><stop offset="1" stop-color="#a8180e"/>
      </linearGradient>
    </defs>
    <rect width="677" height="1571" fill="url(#sheenB)"/>
    <polygon points="0,790 525,790 677,1100 677,1360 0,1360" fill="url(#redB)"/>
    <polygon points="545,790 677,790 677,1065" fill="var(--blue)"/>
    <polygon points="0,808 505,808 575,955 40,955" fill="var(--blue)"/>
    <polygon points="60,1362 677,1362 677,1571 150,1571" fill="var(--blue)"/>
    <polygon points="120,1445 677,1445 677,1530 160,1530" fill="url(#redB)"/>
  </svg>

  <div class="brand"><span class="brand__dot"></span><span class="brand__name">MR TOVEL</span></div>
  <p class="brand__tag">EXPRESS WASH &amp; DETAIL</p>

  <div class="photo-slot" role="img" aria-label="Photo of a smiling car wash worker in red shirt and grey overalls polishing a dark car headlight in a bright showroom"></div>
  <svg class="card__bg" viewBox="0 0 677 1571" preserveAspectRatio="none" aria-hidden="true" style="pointer-events:none">
    <polygon points="515,717 677,717 677,790 545,790" fill="var(--blue)"/>
  </svg>

  <h1 class="abs banner-title" style="left:70px;top:828px;font-size:56px;line-height:.98">UNLIMITED<br>MONTHLY VIP CLUB</h1>

  <h2 class="abs pkg-name" style="left:78px;top:984px">GRAND TOVEL</h2>
  <span class="pkg-line" style="left:60px;top:1026px;width:360px"></span>
  <span class="pkg-line" style="left:440px;top:969px;width:155px"></span>
  <span class="price price--blue" style="left:425px;top:975px">$55</span>
  <p class="abs feature" style="left:78px;top:1042px">includes 10% off detail packages</p>

  <h2 class="abs pkg-name" style="left:78px;top:1097px">ORLA &amp; FINCH</h2>
  <span class="pkg-line" style="left:60px;top:1139px;width:360px"></span>
  <span class="pkg-line" style="left:440px;top:1082px;width:155px"></span>
  <span class="price price--blue" style="left:425px;top:1088px">$45</span>
  <p class="abs feature" style="left:78px;top:1152px">includes 10% off detail packages</p>

  <h2 class="abs pkg-name" style="left:78px;top:1205px">PRIME TOVEL</h2>
  <span class="pkg-line" style="left:60px;top:1247px;width:360px"></span>
  <span class="pkg-line" style="left:440px;top:1192px;width:155px"></span>
  <span class="price price--blue" style="left:425px;top:1198px">$30</span>

  <h2 class="abs pkg-name" style="left:78px;top:1274px">EXPRESS WASH</h2>
  <span class="pkg-line" style="left:60px;top:1315px;width:360px"></span>
  <span class="pkg-line" style="left:440px;top:1261px;width:155px"></span>
  <span class="price price--blue" style="left:425px;top:1267px">$20</span>

  <p class="abs tag-note" style="right:82px;top:1333px">* one wash tag per vehicle</p>

  <p class="abs cta" style="left:150px;width:500px;top:1380px">CALL US NOW</p>
  <p class="abs phone" style="left:170px;top:1456px">
    <svg class="phone__icon" viewBox="0 0 48 48" aria-hidden="true"><circle cx="24" cy="24" r="21" fill="none" stroke="#fff" stroke-width="3"/><path d="M17 13c2-1 3 0 4 3s0 3-1 4c1 3 4 6 7 7 1-1 2-2 4-1s4 2 3 4c-1 3-4 4-7 3-6-2-11-7-13-13-1-3 1-6 3-7z" fill="#fff"/></svg>
    0456 812 307
  </p>
</section>

</body>
</html>
```